Yoga By Marisol Ad for print

I need a print ad designed to go in a brochure for a charity event. I've attached the specs. I need the specs for the 1/2 page ad.
Text for ad:

“E-RYT 200 extensive training with Asana Scholars
Social Media Influencer
Offering group, private and corporate yoga classes
Email: info@yogabymarisol-studio.com
Web: www.yogabymarisol-studio.com
Phone: 480-555-0163
Instagram: @flowofmarisol

Target Market(s)

Yoga practitioners and businesses looking to bring yoga in to their operation.

Font styles to use
Serif
Script

Colors
eda3c7
e34197
eea4c8
f9d9e8
feeeee
000000
1b1b1b
cbcbcb
eaeaea

Requirements
Must have
• One version of my logo, I have provided many to choose from for best aesthetic appeal

```html
<!DOCTYPE html>
<html lang="en">
<head>
<meta charset="utf-8">
<title>Yoga by Marisol – Print Ad</title>
<link rel="stylesheet" href="https://fonts.googleapis.com/css2?family=Raleway:wght@300;400&display=swap">
<style>
  :root {
    --ink: #1b1b1b;
    --ring-1: #2a2a2c;
    --ring-2: #333335;
    --ring-3: #3c3c3e;
    --rose: #e8456a;
    --rose-deep: #c9234b;
    --paper: #ffffff;
    --silver: #cbcbcb;
    --silver-light: #eaeaea;
    --text-dark: #2b2b2b;
    --text-light: #ffffff;
  }
  * { margin: 0; padding: 0; box-sizing: border-box; }
  html, body { width: 916px; height: 1200px; overflow: hidden; background: var(--paper); }
  .ad {
    position: relative;
    width: 916px;
    height: 1200px;
    overflow: hidden;
    background: var(--ink);
    font-family: "Raleway", "Helvetica Neue", Arial, sans-serif;
    font-variant-numeric: lining-nums;
  }
  .ad__backdrop { position: absolute; inset: 0; }
  .portrait {
    position: absolute;
    left: 372px;
    top: 76px;
    width: 528px;
    height: 790px;
    border-radius: 48% 48% 30% 30% / 20% 20% 14% 14%;
    background: linear-gradient(180deg,
      rgba(214,176,150,0.9) 0%,
      rgba(226,196,170,0.9) 35%,
      rgba(255,140,120,0.9) 50%,
      rgba(216,180,156,0.9) 63%,
      rgba(36,140,176,0.95) 78%,
      rgba(30,120,158,0.95) 100%);
  }
  .headline {
    position: absolute;
    left: 0;
    top: 130px;
    width: 420px;
    text-align: center;
    font-weight: 300;
    line-height: 1;
    text-shadow: 0 2px 6px rgba(0,0,0,0.6);
  }
  .headline__main { display: block; color: var(--rose); font-size: 88px; }
  .headline__joiner { display: block; color: var(--text-light); font-size: 56px; margin: 12px 0 10px; }
  .credentials {
    position: absolute;
    left: 55px;
    top: 510px;
    width: 300px;
    text-align: center;
    color: var(--text-light);
    font-size: 25px;
    font-weight: 300;
    line-height: 1.32;
    list-style: none;
  }
  .credentials li + li::before {
    content: "";
    display: block;
    width: 158px;
    height: 2px;
    margin: 14px auto 14px;
    background: var(--rose);
  }
  .brand-seal {
    position: absolute;
    left: 637px;
    top: 880px;
    width: 232px;
    height: 232px;
    border-radius: 50%;
    background: var(--paper);
    border: 8px solid var(--silver);
    box-shadow: 0 0 0 2px var(--silver-light), 0 4px 10px rgba(0,0,0,0.35);
    display: flex;
    align-items: center;
    justify-content: center;
  }
  .brand-seal__name {
    color: var(--rose);
    font-size: 30px;
    font-weight: 400;
    text-align: center;
    line-height: 1.1;
  }
  .contacts {
    position: absolute;
    left: 40px;
    top: 1082px;
    display: grid;
    grid-template-columns: 420px 240px;
    row-gap: 14px;
    list-style: none;
    color: var(--text-dark);
    font-size: 24px;
    font-weight: 400;
  }
  .contacts li { display: flex; align-items: center; gap: 14px; height: 32px; white-space: nowrap; }
  .contacts svg { flex: none; }
</style>
</head>
<body>
<main class="ad">
  <svg class="ad__backdrop" width="916" height="1200" viewBox="0 0 916 1200" aria-hidden="true">
    <circle cx="620" cy="520" r="340" fill="var(--ring-1)"/>
    <circle cx="625" cy="555" r="280" fill="var(--ring-2)"/>
    <circle cx="632" cy="585" r="200" fill="var(--ring-3)"/>
    <path d="M0 0 H400 C330 20 250 50 150 50 C90 50 40 40 0 30 Z" fill="var(--rose-deep)"/>
    <path d="M0 0 H330 C270 18 200 36 120 36 C70 36 30 30 0 22 Z" fill="var(--rose)"/>
  </svg>

  <div class="portrait" role="img" aria-label="Photo of the instructor seated cross-legged with arms stretched overhead, wearing a coral top and blue leggings"></div>

  <svg class="ad__backdrop" width="916" height="1200" viewBox="0 0 916 1200" aria-hidden="true">
    <path d="M0 940 C140 900 300 930 430 975 C520 1005 580 1012 660 1002 L916 960 V1200 H0 Z" fill="var(--rose-deep)"/>
    <path d="M0 955 C150 915 300 950 420 990 C520 1020 600 1020 680 1010 L916 975 V1200 H0 Z" fill="var(--rose)"/>
    <path d="M420 955 C500 975 580 985 660 978 L660 992 C580 998 500 990 420 962 Z" fill="var(--rose)"/>
    <path d="M0 1000 C160 975 320 1000 460 1022 C560 1036 640 1036 720 1020 C800 1000 860 950 916 880 V1200 H0 Z" fill="var(--paper)"/>
  </svg>

  <h1 class="headline">
    <span class="headline__main">Yoga</span>
    <span class="headline__joiner">by</span>
    <span class="headline__main">Marisol</span>
  </h1>

  <ul class="credentials">
    <li>E-RYT 200 extensive training with Asana Scholars</li>
    <li>Social Media Influencer</li>
    <li>Offering group, private and corporate yoga classes</li>
  </ul>

  <div class="brand-seal">
    <span class="brand-seal__name">Marisol<br>Flow</span>
  </div>

  <ul class="contacts">
    <li>
      <svg width="28" height="22" viewBox="0 0 28 22" aria-hidden="true"><rect x="1" y="1" width="26" height="20" rx="3" fill="var(--rose)"/><path d="M3 4 L14 12 L25 4" fill="none" stroke="var(--paper)" stroke-width="2"/></svg>
      info@yogabymarisol-studio.com
    </li>
    <li>
      <svg width="26" height="26" viewBox="0 0 26 26" aria-hidden="true"><path d="M7 2 L11 7 L8 10 C9 13 13 17 16 18 L19 15 L24 19 L21 24 C12 23 3 14 2 5 Z" fill="var(--rose)"/></svg>
      480-555-0163
    </li>
    <li>
      <svg width="28" height="28" viewBox="0 0 28 28" aria-hidden="true"><g fill="none" stroke="var(--rose)" stroke-width="2.4"><circle cx="14" cy="14" r="12"/><ellipse cx="14" cy="14" rx="5" ry="12"/><path d="M2 14 H26 M4 8 H24 M4 20 H24"/></g></svg>
      www.yogabymarisol-studio.com
    </li>
    <li>
      <svg width="26" height="26" viewBox="0 0 26 26" aria-hidden="true"><rect x="1" y="1" width="24" height="24" rx="4" fill="var(--rose)"/></svg>
      @flowofmarisol
    </li>
  </ul>
</main>
</body>
</html>
```